Dubai, Oman, Saudi, Qatar, Kuwait, Bahrain
OVUX.CA a popular Canadian non profit is opening in the middle east and will require a website that appeals to the Arab world
Industry
Technology
Color Preferences
green and blue and similar to ovux.ca
Our Ideas & Additional Information
use these websites as examples to copy and make similar websites
www.pqz.mg
www.ovux.ca
www.lirovastemo.ba
OVUX Arabic - Zafir Tech (Technology) non profit , foundation , association
Please try to use some arabic writing as well as latin alphabet for the name of the company
Zafir Tech (Technology)
Please see sample logos attached, dont worry about logo design we will add later
Target Market(s)
gcc
Number of Pages Required
1 page
Look and feel

```html
<!DOCTYPE html>
<html lang="en">
<head>
<meta charset="utf-8">
<title>ovux.renew.collective — Empowering Communities</title>
<link rel="stylesheet" href="https://fonts.googleapis.com/css2?family=Open+Sans:wght@300;400;500;600;700&display=swap">
<style>
:root{
  --blue:#0b6fc8;
  --blue-deep:#0a4a8c;
  --green:#6cc24a;
  --green-light:#8fe35c;
  --green-dark:#3f9b36;
  --ink:#222;
  --muted:#555;
  --line:#d8d8d8;
  --field:#f1f1f1;
  --white:#fff;
}
*{box-sizing:border-box;margin:0;padding:0}
html,body{width:1200px;height:4399px;overflow:hidden}
body{position:relative;font-family:"Open Sans",sans-serif;color:var(--ink);background:var(--white)}
.abs{position:absolute}
.btn{position:absolute;display:flex;align-items:center;justify-content:center;border-radius:22px;font-size:15px;font-weight:500;color:var(--white);background:linear-gradient(90deg,var(--green-light),var(--green-dark));box-shadow:0 3px 6px rgba(0,0,0,.15)}
.btn-outline{background:var(--white);color:var(--ink);border:2px solid var(--green);box-shadow:none}

/* header */
.site-header{position:absolute;left:0;top:0;width:1200px;height:90px;background:var(--white);border-bottom:2px solid #e8e8e8}
.brand{position:absolute;left:60px;top:22px;display:flex;align-items:center;gap:10px;font-size:14px;color:var(--blue);font-weight:500}
.brand-dot{width:46px;height:46px;border-radius:50%;border:3px solid var(--green)}
.nav{position:absolute;left:464px;top:36px;display:flex;gap:33px;font-size:13px;color:#444}

/* hero */
.hero{position:absolute;left:0;top:90px;width:1200px;height:630px;background:linear-gradient(180deg,#fff 0%,#fff 35%,#e5f0fb 75%,#fff 100%)}
.skyline{position:absolute;left:0;top:260px;width:600px;height:290px;background:linear-gradient(180deg,rgba(160,200,235,.15),rgba(140,190,235,.45))}
.hero h1{position:absolute;left:60px;top:110px;font-size:72px;line-height:76px;font-weight:600;color:var(--blue);letter-spacing:-.5px}
.hero .tagline{position:absolute;left:60px;top:265px;font-size:25px;color:var(--green)}
.hero p{position:absolute;left:60px;top:325px;width:450px;font-size:12.5px;line-height:22px;color:var(--muted)}
.hero-art{position:absolute;left:600px;top:20px;width:540px;height:570px;border-radius:200px 200px 270px 270px;background:radial-gradient(ellipse at 50% 80%,#ffffff 0%,#eef6ea 35%,rgba(0,0,0,0) 36%),linear-gradient(160deg,#9be06f,#56b93b 60%,#3d8f2f)}

/* about */
.about-bar{position:absolute;left:95px;top:750px;width:230px;height:375px;border-radius:10px;background:linear-gradient(180deg,var(--green-light),var(--green-dark))}
.about-photo{position:absolute;left:140px;top:750px;width:440px;height:350px;border-radius:6px;background:linear-gradient(180deg,#5f7fa0 0%,#b89a86 55%,#4b5a66 100%)}
.years{position:absolute;left:118px;top:1050px;display:flex;align-items:center;gap:10px;color:var(--white)}
.years b{font-size:40px;font-weight:500}
.years span{font-size:17px;line-height:22px}
.about-text{position:absolute;left:640px;top:755px;width:460px;text-align:center}
.about-text h2{font-size:38px;font-weight:500;color:var(--blue)}
.about-text p{font-size:12.5px;line-height:22px;color:var(--muted);margin-top:20px}
.about-text h2+p{margin-top:50px}

/* certifications */
.certs{position:absolute;left:0;top:1200px;width:1200px;height:425px;background:linear-gradient(135deg,var(--green-light),var(--green-dark))}
.certs h2{position:absolute;left:0;top:48px;width:1200px;text-align:center;color:var(--white);font-size:37px;line-height:52px;font-weight:500}
.badge{position:absolute;top:197px;width:176px;height:176px;border-radius:50%;background:var(--white);border:6px solid #dfeef9}

/* process */
.process h2{position:absolute;left:0;top:1700px;width:1200px;text-align:center;font-size:38px;font-weight:500;color:var(--blue)}
.row{position:absolute;left:60px;width:1080px;height:92px;border-top:1px solid var(--line);display:flex;align-items:center}
.row .num{width:90px;font-size:34px;font-weight:300}
.row .num small{font-size:20px;margin-left:6px}
.row .title{width:348px;font-size:27px;font-weight:400}
.row .desc{width:320px;font-size:12.5px;line-height:22px;color:var(--muted)}
.process-photo{position:absolute;left:838px;top:1800px;width:220px;height:230px;border-radius:28px;transform:rotate(14deg);background:linear-gradient(150deg,#a7b9c9,#6a7f92 60%,#2f3e4d)}
.arrow{position:absolute;left:1079px;width:60px;height:60px;border-radius:50%;display:flex;align-items:center;justify-content:center}
.arrow.green{background:linear-gradient(135deg,var(--green-light),var(--green-dark))}
.arrow.blue{background:#1371d6}

/* gcc */
.gcc h2{position:absolute;left:130px;top:2222px;width:400px;text-align:center;font-size:38px;font-weight:500;color:var(--blue)}
.checks{position:absolute;left:95px;top:2320px;width:460px;list-style:none}
.checks li{position:relative;padding-left:22px;font-size:12.5px;line-height:22px;color:var(--muted);margin-bottom:18px}
.checks li svg{position:absolute;left:0;top:6px}
.gcc-bar{position:absolute;left:875px;top:2218px;width:229px;height:374px;border-radius:6px;background:linear-gradient(180deg,var(--green-dark),var(--green-light))}
.gcc-photo{position:absolute;left:620px;top:2218px;width:438px;height:350px;background:linear-gradient(160deg,#cdbfae,#e9e3dc 45%,#8d8479)}

/* services */
.services{position:absolute;left:0;top:2667px;width:1200px;height:713px;background:linear-gradient(160deg,#1066c8,#074c97 60%,#063f7c)}
.services h2{position:absolute;left:0;top:55px;width:1200px;text-align:center;font-size:38px;font-weight:500;color:var(--white)}
.vline{position:absolute;left:599px;width:2px;background:rgba(255,255,255,.7)}
.hline{position:absolute;top:404px;height:2px;background:rgba(255,255,255,.7)}
.hub{position:absolute;left:530px;top:335px;width:140px;height:140px;border-radius:50%;background:var(--white);display:flex;align-items:center;justify-content:center;font-size:26px;color:var(--blue);border:8px solid #e4f3dc}
.svc{position:absolute;width:340px;text-align:center;color:var(--white)}
.svc svg{display:block;margin:0 auto 22px}
.svc h3{font-size:19px;font-weight:400;margin-bottom:14px}
.svc p{font-size:12.5px;line-height:20px;width:260px;margin:0 auto}

/* contact */
.contact h2{position:absolute;left:77px;top:3505px;font-size:40px;font-weight:500;color:var(--blue)}
.contact .intro{position:absolute;left:77px;top:3572px;width:530px;font-size:12.5px;line-height:22px;color:var(--muted)}
.info{position:absolute;left:77px;display:flex;gap:16px;align-items:flex-start}
.info b{display:block;font-size:17px;font-weight:500}
.info span{font-size:14px;color:#444}
.socials{position:absolute;left:77px;top:3920px;display:flex;gap:20px}
.socials i{width:31px;height:31px;border-radius:50%;background:var(--green);display:block}
.form-card{position:absolute;left:650px;top:3450px;width:475px;height:510px;border:3px solid #eee;border-radius:14px;box-shadow:0 3px 10px rgba(0,0,0,.06)}
.field{position:absolute;left:33px;width:407px;height:50px;background:var(--field);border-radius:4px;font-size:12.5px;color:#666;padding:17px 23px}
.submit{left:33px;width:407px;height:40px;top:482px;font-size:15px;border-radius:20px}

/* footer */
.site-footer{position:absolute;left:0;top:4095px;width:1200px;height:304px;background:linear-gradient(180deg,#6fc54c,#62b943)}
.foot-logo{position:absolute;left:65px;top:45px;width:100px;height:100px;border-radius:50%;border:5px solid var(--white);display:flex;align-items:center;justify-content:center;color:var(--white);font-size:22px}
.foot-name{position:absolute;left:183px;top:78px;font-size:28px;color:var(--white)}
.foot-info{position:absolute;left:775px;font-size:12.5px;color:var(--white);display:flex;gap:10px;align-items:center}
.foot-social{position:absolute;left:775px;top:132px;display:flex;gap:16px;align-items:center;color:var(--white);font-size:12.5px}
.foot-social i{width:13px;height:13px;background:var(--white);border-radius:2px;display:block}
.foot-rule{position:absolute;left:60px;top:227px;width:1080px;height:1px;background:rgba(255,255,255,.6)}
.foot-nav{position:absolute;left:60px;top:252px;display:flex;gap:32px;font-size:11px;color:var(--white)}
.copy{position:absolute;right:60px;top:252px;font-size:11px;color:var(--white)}
</style>
</head>
<body>

<header class="site-header">
  <div class="brand"><span class="brand-dot"></span>ovux.renew.collective</div>
  <nav class="nav"><span>Home</span><span>About OVUX</span><span>Mission</span><span>GCC Countries Focus</span><span>What We Do</span></nav>
  <div class="btn" style="left:988px;top:24px;width:132px;height:41px">Contact Us</div>
</header>

<section class="hero">
  <div class="skyline" role="img" aria-label="Faint city skyline illustration"></div>
  <h1>Empowering<br>Communities</h1>
  <div class="tagline">Through Technology &amp; Sustainability</div>
  <p>Lorem Ipsum Dolor Sit Amet Consectetur. Neque Faucibus Morbi Integer Nam Pellentesque. Molestie Mi Duis Dui Convallis Lorem Magna Quam Id. Neque Facilisis Tristique Libero Faucibus Porttitor Id Arcu Neque Arcu. Felis At Faucibus At Turpis Ornare Odio.</p>
  <div class="btn" style="left:60px;top:475px;width:132px;height:38px">Donate Tech</div>
  <div class="btn btn-outline" style="left:222px;top:475px;width:133px;height:38px">Get Involved</div>
  <div class="hero-art" role="img" aria-label="Illustration of a green recycling bin filled with old computers and devices in front of green buildings"></div>
</section>

<section class="about">
  <div class="about-bar"></div>
  <div class="about-photo" role="img" aria-label="Photo of a Gulf city skyline at sunset"></div>
  <div class="years"><b>25+</b><span>Years Of<br>Experience</span></div>
  <div class="about-text">
    <h2>About OVUX Arabia</h2>
    <p>Lorem Ipsum Dolor Sit Amet Consectetur. Leo Nibh Eget Sit Convallis Sit Aenean. Morbi Faucibus Augue Ullamcorper Vel Bibendum. Amet Nisi Orci Varius Semper Nunc. Aliquam Proin Purus Volutpat Euismod Condimentum. Facilisi Massa Pharetra Aenean Tortor Sit Risus Ultricies At Ultrices. In Interdum Nulla Id Commodo Nisi Diam. Pulvinar Id Amet.</p>
    <p>Lorem Ipsum Dolor Sit Amet Consectetur. Et Ultricies Nisi Sit Et Proin Aenean Faucibus.</p>
  </div>
  <div class="btn" style="left:790px;top:1078px;width:158px;height:40px">Discover More</div>
</section>

<section class="certs">
  <h2>OVUX’s ISO-Certified Excellence in Security<br>Quality &amp; Sustainability</h2>
  <div class="badge" style="left:134px" role="img" aria-label="Certification badge"></div>
  <div class="badge" style="left:387px" role="img" aria-label="Certification badge"></div>
  <div class="badge" style="left:625px" role="img" aria-label="Certification badge"></div>
  <div class="badge" style="left:883px" role="img" aria-label="Certification badge"></div>
</section>

<section class="process">
  <h2>How Ovux.Renew.Collective Works</h2>
  <div class="row" style="top:1865px"><span class="num">01<small>/</small></span><span class="title">Tech Recycling</span><span class="desc">We collect and recycle used electronics to reduce e-waste.</span></div>
  <div class="row" style="top:1957px"><span class="num">02<small>/</small></span><span class="title">Device Donations</span><span class="desc">Refurbished computers are donated to schools, NGOs, and low-income families.</span></div>
  <div class="row" style="top:2049px;border-bottom:1px solid var(--line)"><span class="num">03<small>/</small></span><span class="title">Digital Education</span><span class="desc">We promote digital literacy and equal access to technology.</span></div>
  <div class="process-photo" role="img" aria-label="Photo of a smiling man on the phone at his desk"></div>
  <div class="arrow green" style="top:1878px"><svg width="24" height="24" viewBox="0 0 24 24" fill="none" stroke="#fff" stroke-width="2"><path d="M5 5l14 14M19 8v11H8"/></svg></div>
  <div class="arrow blue" style="top:1970px"><svg width="24" height="24" viewBox="0 0 24 24" fill="none" stroke="#fff" stroke-width="2"><path d="M5 5l14 14M19 8v11H8"/></svg></div>
  <div class="arrow blue" style="top:2062px"><svg width="24" height="24" viewBox="0 0 24 24" fill="none" stroke="#fff" stroke-width="2"><path d="M5 5l14 14M19 8v11H8"/></svg></div>
</section>

<section class="gcc">
  <h2>Our Work In The GCC</h2>
  <ul class="checks">
    <li><svg width="12" height="10" viewBox="0 0 12 10" fill="none" stroke="#6cc24a" stroke-width="2"><path d="M1 5l3.5 3.5L11 1"/></svg>Lorem Ipsum Dolor Sit Amet Consectetur. Eu Viverra Nunc Nibh Dictum Mattis Sit. Diam Sagittis Convallis</li>
    <li><svg width="12" height="10" viewBox="0 0 12 10" fill="none" stroke="#6cc24a" stroke-width="2"><path d="M1 5l3.5 3.5L11 1"/></svg>Lorem Ipsum Dolor Sit Amet Consectetur. Pharetra Feugiat Cursus Non Ipsum Consequat Tristique Venenatis Tincidunt.</li>
    <li><svg width="12" height="10" viewBox="0 0 12 10" fill="none" stroke="#6cc24a" stroke-width="2"><path d="M1 5l3.5 3.5L11 1"/></svg>Lorem Ipsum Dolor Sit Amet Consectetur. Et Ultricies Nisi Sit Et Proin Aenean Faucibus.</li>
  </ul>
  <div class="btn" style="left:253px;top:2548px;width:157px;height:38px">Discover More</div>
  <div class="gcc-bar"></div>
  <div class="gcc-photo" role="img" aria-label="Photo of a team working together around a laptop"></div>
</section>

<section class="services">
  <h2>What We Do</h2>
  <div class="vline" style="top:158px;height:148px"></div>
  <div class="vline" style="top:508px;height:148px"></div>
  <div class="hline" style="left:150px;width:350px"></div>
  <div class="hline" style="left:700px;width:348px"></div>
  <div class="hub">ovux.ca</div>

  <div class="svc" style="left:153px;top:150px">
    <svg width="78" height="62" viewBox="0 0 78 62" fill="none" stroke="#fff" stroke-width="2.5"><rect x="12" y="4" width="54" height="38" rx="2"/><path d="M3 48h72l-5 8H8z"/></svg>
    <h3>Donate Your Used Electronics</h3>
    <p>Give Your Unused Devices A Second Life — We Refurbish And Donate Them To Those In Need.</p>
  </div>
  <div class="svc" style="left:703px;top:150px">
    <svg width="70" height="62" viewBox="0 0 70 62" fill="none" stroke="#fff" stroke-width="2.5"><path d="M4 26l14-14 12 6 10-4 12 4 14 12"/><path d="M18 30l14 14a4 4 0 006-6L28 28M26 40l8 8a4 4 0 006-6M40 36l6 6a4 4 0 006-6L40 24"/><path d="M35 2v6M24 5l3 5M46 5l-3 5"/></svg>
    <h3>Become a Partner</h3>
    <p>Partner With Us As A Business, School, Or Organization To Expand Our Impact In The GCC.</p>
  </div>
  <div class="svc" style="left:153px;top:468px">
    <svg width="70" height="70" viewBox="0 0 70 70" fill="none" stroke="#fff" stroke-width="2.5"><path d="M8 8l26 26M34 34l8 8M10 62l24-24M62 10L38 34"/><rect x="50" y="4" width="14" height="10" transform="rotate(45 57 9)"/><path d="M4 4l8 2 2 8"/><rect x="20" y="44" width="30" height="20" rx="3"/></svg>
    <h3>Volunteer Your Time</h3>
    <p>Join Our Team To Help Refurbish Devices, Teach Digital Skills, Or Support Local Events.</p>
  </div>
  <div class="svc" style="left:703px;top:468px">
    <svg width="70" height="70" viewBox="0 0 70 70" fill="none" stroke="#fff" stroke-width="2.5"><path d="M10 38l30-26v44L10 44z"/><path d="M16 44l6 18h8l-4-16"/><path d="M50 20l10-8M52 34h12M50 48l10 8"/></svg>
    <h3>Spread the Word</h3>
    <p>Help Us Grow By Sharing Our Mission With Your Network And Community.</p>
  </div>
</section>

<section class="contact">
  <h2>Contact Us</h2>
  <p class="intro">Lorem Ipsum Dolor Sit Amet Consectetur. Viverra Eu Ac Maecenas Ut Aenean Sollicitudin Vel. Posuere Ipsum Cras Vestibulum Nisi. Aliquam Risus Mauris Placerat Fermentum In Ipsum. Et Iaculis Diam Massa Ultrices.</p>
  <div class="info" style="top:3688px">
    <svg width="40" height="40" viewBox="0 0 40 40" fill="none" stroke="#6cc24a" stroke-width="2"><path d="M8 4l7 8-4 5c2 5 6 9 11 11l5-4 8 7-5 6C16 36 4 24 3 10z"/><path d="M24 10a8 8 0 016 6M24 4a14 14 0 0112 12"/></svg>
    <div><b>Call Us</b><span>(604) 555-0188</span></div>
  </div>
  <div class="info" style="top:3758px">
    <svg width="44" height="40" viewBox="0 0 44 40" fill="none" stroke="#6cc24a" stroke-width="2"><rect x="2" y="6" width="32" height="24" rx="2"/><path d="M2 8l16 12 16-12"/><circle cx="36" cy="30" r="6"/></svg>
    <div><b>Email Us</b><span>hello@ovuxmail.net</span></div>
  </div>
  <div class="info" style="top:3828px">
    <svg width="40" height="44" viewBox="0 0 40 44" fill="none" stroke="#6cc24a" stroke-width="2"><path d="M20 42S6 26 6 16a14 14 0 0128 0c0 10-14 26-14 26z"/><circle cx="20" cy="16" r="5"/></svg>
    <div><b>Address</b><span>4120 Palm Grove Rd. Westfield, Ontario 55120</span></div>
  </div>
  <div class="socials"><i></i><i></i><i></i><i></i></div>

  <form class="form-card">
    <div class="field" style="top:37px">Name</div>
    <div class="field" style="top:102px">Email</div>
    <div class="field" style="top:167px">Phone Number</div>
    <div class="field" style="top:232px;height:215px">Message</div>
    <div class="btn submit">Submit Now</div>
  </form>
</section>

<footer class="site-footer">
  <div class="foot-logo">ovux.ca</div>
  <div class="foot-name">ovux.renew.collective</div>
  <div class="foot-info" style="top:50px"><svg width="20" height="16" viewBox="0 0 20 16" fill="none" stroke="#fff" stroke-width="1.5"><path d="M1 8L19 1 14 15 9 10z"/></svg>Delta Bureau, 45 North, 9th Street, Halden 20450</div>
  <div class="foot-info" style="top:82px"><svg width="18" height="18" viewBox="0 0 40 40" fill="none" stroke="#fff" stroke-width="3"><path d="M8 4l7 8-4 5c2 5 6 9 11 11l5-4 8 7-5 6C16 36 4 24 3 10z"/></svg>321 654-0987
    <svg style="margin-left:22px" width="22" height="16" viewBox="0 0 22 16" fill="none" stroke="#fff" stroke-width="1.5"><rect x="1" y="1" width="20" height="14" rx="1"/><path d="M1 2l10 7 10-7"/></svg>Mira.Hollis@Sample.Net</div>
  <div class="foot-social">Social Media <i></i><i></i><i></i><i></i><i></i><i></i><i></i><i></i></div>
  <div class="foot-rule"></div>
  <nav class="foot-nav"><span>Home</span><span>About OVUX</span><span>Mission</span><span>GCC Countries Focus</span><span>What We Do</span></nav>
  <div class="copy">Copyright © 2025All Right Reserved</div>
</footer>

</body>
</html>
```